Kelmora Legal Business Card

I require a corporate business card for a new legal services business.

I do not have a logo, nor do I want one.

I require a clean, neat a professional card for a law firm.

Details:

Business Name: Kelmora Legal
Name: Debra Lindqvist
Title: Corporate Services Manager
Location: Office 14 (Top Floor), Toravel Business Centre, Quinlan Grove Street, Alotau CBD, Milne Bay Province.
Postal Address: PO Box 593, Alotau, 211, Milne Bay Province, Papua New Guinea.
Contact: T: +675 6418250, F: +675 6413362, M: +675 72915867, E: dlindqvist@kelmoraexample.com.pg.

I look forward to your design submissions.

Industry/Entity Type

Legal

```html
<!DOCTYPE html>
<html lang="en">
<head>
<meta charset="utf-8">
<title>Kelmora Legal – Business Card</title>
<link rel="stylesheet" href="https://fonts.googleapis.com/css2?family=Questrial&display=swap">
<style>
  :root {
    --card-bg: #d7d5bb;
    --ink: #545456;
    --rule-light: #ffffff;
  }
  * { margin: 0; padding: 0; box-sizing: border-box; }
  html, body {
    width: 1200px;
    height: 734px;
    overflow: hidden;
    background: var(--card-bg);
  }
  .card {
    position: relative;
    width: 1200px;
    height: 734px;
    background: var(--card-bg);
    color: var(--ink);
    font-family: "Questrial", "Century Gothic", sans-serif;
    line-height: 1;
  }
  .card__rules {
    position: absolute;
    inset: 0;
  }
  .card__text { position: absolute; white-space: nowrap; }
  .firm-name {
    left: 0; width: 1220px; text-align: center;
    top: 100px;
    font-size: 96px;
    letter-spacing: 1px;
  }
  .person-name {
    left: 0; width: 1226px; text-align: center;
    top: 262px;
    font-size: 45px;
    letter-spacing: 4px;
  }
  .person-role {
    left: 0; width: 1246px; text-align: center;
    top: 311px;
    font-size: 26px;
    letter-spacing: 0.5px;
  }
  .address {
    top: 419px;
    font-size: 29px;
    line-height: 37.3px;
  }
  .address--street { left: 34px; text-align: left; }
  .address--postal { right: 37px; text-align: right; }
  .contact-line {
    left: 0; width: 1200px; text-align: center;
    top: 617px;
    font-size: 22px;
  }
</style>
</head>
<body>
<main class="card">
  <svg class="card__rules" width="1200" height="734" viewBox="0 0 1200 734" aria-hidden="true">
    <defs>
      <linearGradient id="rule-fade" x1="0" x2="1" y1="0" y2="0">
        <stop offset="0" stop-color="#ffffff" stop-opacity="0"/>
        <stop offset="0.5" stop-color="#ffffff" stop-opacity="1"/>
        <stop offset="1" stop-color="#ffffff" stop-opacity="0"/>
      </linearGradient>
    </defs>
    <rect x="68" y="72.5" width="1064" height="4" fill="url(#rule-fade)"/>
    <circle cx="600" cy="50" r="11" fill="var(--rule-light)"/>
    <rect x="68" y="657" width="1064" height="4" fill="url(#rule-fade)"/>
    <circle cx="600" cy="684" r="11" fill="var(--rule-light)"/>
  </svg>

  <h1 class="card__text firm-name">Kelmora Legal</h1>
  <p class="card__text person-name">Debra Lindqvist</p>
  <p class="card__text person-role">Corporate Services Manager</p>

  <address class="card__text address address--street" style="font-style:normal">
    Office 14 (Top Floor)<br>
    Toravel Business Centre<br>
    Quinlan Grove Street<br>
    Alotau CBD, Milne Bay Province
  </address>

  <address class="card__text address address--postal" style="font-style:normal">
    PO Box 593<br>
    Alotau, 211<br>
    Milne Bay Province<br>
    Papua New Guinea
  </address>

  <p class="card__text contact-line">T: +675 6418250 &nbsp;|&nbsp; F: +675 6413362 &nbsp;|&nbsp; M: +675 72915867 | E: dlindqvist@kelmoraexample.com.pg</p>
</main>
</body>
</html>
```